Business card design Brightvane

We need a business card for BRIGHTvane aimport and distribution company which sells personnel weight lifting accessories, mainly the dorvel brand of product using our current logo. This design should represent class and a ruggard feel.

Target Market(s)

Weight lifters, crossfitters and other lifting sports

Industry/Entity Type

Weight

Contact Information for Business Card

BRIGHTvane, Owen Palfrey, Cell: 027 918 603, Email: brightvane@mailnest.co.nz, www.brightvane.co.nz

Requirements
Nice to have
• a good looking business card

```html
<!DOCTYPE html>
<html lang="en">
<head>
<meta charset="utf-8">
<title>Brightvane — Business Card</title>
<link rel="stylesheet" href="https://fonts.googleapis.com/css2?family=Arimo:wght@400;700&family=Parisienne&display=swap">
<style>
  :root {
    --backdrop: #e9ebee;
    --card: #ffffff;
    --card-back: #f3f3f3;
    --ink: #333333;
    --brand-blue: #1f4e8c;
    --edge-warm: #f7941d;
    --edge-mid: #8e3f98;
    --edge-cool: #8dc63f;
    --seal-red: #f23c3c;
    --icon-phone: #ef3b3b;
    --icon-email: #8dc63f;
    --icon-web: #1ab0e8;
  }
  * { box-sizing: border-box; margin: 0; padding: 0; }
  html, body {
    width: 1200px; height: 900px; overflow: hidden;
    background: var(--backdrop);
    font-family: "Arimo", Arial, sans-serif;
  }
  .canvas {
    width: 1200px; height: 900px;
    display: flex; justify-content: center; align-items: center; gap: 120px;
  }
  .card {
    position: relative;
    width: 330px; height: 578px;
    background: var(--card);
    box-shadow: 0 6px 18px rgba(0,0,0,0.18);
    overflow: hidden;
  }
  .card--back { background: var(--card-back); display: flex; justify-content: center; align-items: center; }

  .edge-band {
    position: absolute; left: 0; top: 0; bottom: 0; width: 30px;
    background: linear-gradient(to bottom, var(--edge-warm), var(--edge-mid) 50%, var(--edge-cool));
  }

  .brand-name {
    font-family: "Arimo", Arial, sans-serif;
    font-weight: 700;
    color: var(--brand-blue);
    letter-spacing: 0.5px;
    white-space: nowrap;
  }
  .card--front .brand-name {
    position: absolute; top: 88px; left: 70px;
    font-size: 34px;
  }
  .card--back .brand-name { font-size: 42px; }

  .holder-name {
    position: absolute; top: 200px; left: 64px;
    font-family: "Parisienne", cursive;
    font-size: 38px;
    color: var(--brand-blue);
    letter-spacing: 2px;
    white-space: nowrap;
  }
  .contact-list {
    position: absolute; top: 292px; left: 70px;
    list-style: none;
    font-size: 15px; color: var(--ink); line-height: 24px;
  }
  .contact-list li { display: flex; align-items: center; gap: 8px; white-space: nowrap; }
  .contact-icon {
    width: 13px; height: 13px; border-radius: 3px;
    color: #fff; font-size: 9px; font-weight: 700;
    display: inline-flex; justify-content: center; align-items: center;
  }
  .contact-icon--phone { background: var(--icon-phone); }
  .contact-icon--email { background: var(--icon-email); }
  .contact-icon--web   { background: var(--icon-web); }

  .seal {
    position: absolute; right: 46px; bottom: 76px;
    width: 118px; height: 118px; border-radius: 50%;
    background: var(--seal-red);
  }
</style>
</head>
<body>
<main class="canvas">
  <article class="card card--front" aria-label="Business card front">
    <div class="edge-band" role="img" aria-label="Multicolour decorative edge band"></div>
    <div class="brand-name">BRIGHTvane</div>
    <div class="holder-name">Owen Palfrey</div>
    <ul class="contact-list">
      <li><span class="contact-icon contact-icon--phone">t</span>027 918 603</li>
      <li><span class="contact-icon contact-icon--email">e</span>brightvane@mailnest.co.nz</li>
      <li><span class="contact-icon contact-icon--web">w</span>www.brightvane.co.nz</li>
    </ul>
    <div class="seal" role="img" aria-label="Red decorative seal"></div>
  </article>

  <article class="card card--back" aria-label="Business card back">
    <div class="brand-name">BRIGHTvane</div>
  </article>
</main>
</body>
</html>
```